依頼詳細
当サイトに店舗情報等を掲載してもらうための店舗への説明用チラシのデザイン制作をお願い致します。思わず掲載をしたくなるようなデザインをお願いします。シンプルでわかり易いものが希望です。
記載項目
サイト名はsemu(セム)・店舗情報掲載料1P21,000円/年額 複数P(写真・メニュー・クーポン等)42,000円/年額 求人情報掲載無料・採用時31,500円 当サイトの収益は児童養護施設等の子供達の学習支援に使われます。
サイズ
A4
ページ数
片面
希望イメージ
シンプル 複雑
単色 カラフル
暗い 明るい
日常 高級
遊び心 厳粛
未来的 伝統的
女性的 男性的
希望する色
オレンジ
納品ファイル
• 高解像度JPG (.jpg)
• イラストレーター形式 (.ai)
補足説明
《選ぶワクワクを全ての人に》をミッションにしたNPOです。この度開設するサイトを通じて、大人の生活の選択肢を増やし、学習支援によって子どもの将来の選択肢を増やすことを目的としています。サイト開設にあたっては、一定数の店舗登録が必須なため、店舗への説明がわかりやすい営業用チラシが必要です。イメージとしてはひらけ堂やぽみたすが近いかと思います。

```html
<!DOCTYPE html>
<html lang="ja">
<head>
<meta charset="utf-8">
<title>セム 店舗掲載のご案内</title>
<link rel="stylesheet" href="https://fonts.googleapis.com/css2?family=Anton&family=M+PLUS+Rounded+1c:wght@800;900&family=Noto+Sans+JP:wght@700;900&display=swap">
<style>
:root{
  --orange:#f39200;
  --orange-deep:#e86f00;
  --yellow:#fff100;
  --red:#e60012;
  --white:#ffffff;
  --ink:#222222;
  --photo:#e9c9b0;
  --screen:#f4efe6;
}
*{margin:0;padding:0;box-sizing:border-box}
html,body{width:848px;height:1200px;overflow:hidden}
body{background:var(--orange);font-family:"Noto Sans JP",sans-serif;color:var(--white)}
.flyer{position:relative;width:848px;height:1200px;overflow:hidden;background:var(--orange)}
.tagline{position:absolute;left:22px;top:24px;font-size:27px;font-weight:900;line-height:1.2;white-space:nowrap}
.site-name{position:absolute;left:0;width:848px;top:80px;text-align:center;font-family:"Anton",sans-serif;font-size:270px;line-height:1;color:var(--yellow);letter-spacing:10px}
.model-photo{position:absolute;left:0;top:370px;width:450px;height:560px;background:linear-gradient(160deg,#f2d9c4 0%,var(--photo) 55%,#f6f0ea 100%);border-radius:0 140px 0 0}
.bubble{position:absolute;left:380px;top:385px;width:450px;height:175px}
.bubble-text{position:absolute;left:430px;top:402px;width:390px;font-size:36px;font-weight:900;color:var(--ink);line-height:66px;text-align:center;white-space:nowrap}
.bubble-text .accent{color:var(--orange-deep);font-size:48px}
.phone{position:absolute;left:450px;top:575px;width:265px;height:400px;background:#1b1b1b;border-radius:34px}
.phone-screen{position:absolute;left:466px;top:625px;width:233px;height:300px;background:linear-gradient(180deg,#ffffff 0%,var(--screen) 100%)}
.phone-button{position:absolute;left:569px;top:935px;width:28px;height:28px;border:3px solid #555;border-radius:50%}
.genre-list{position:absolute;left:24px;top:738px;list-style:none;font-size:28px;font-weight:900;line-height:40px}
.genre-list li{display:block;margin-bottom:2px;white-space:nowrap}
.genre-list .tag{background:var(--yellow);color:var(--orange-deep);padding:0 8px}
.price-label{position:absolute;left:24px;top:940px;background:var(--red);font-size:26px;font-weight:900;line-height:36px;padding:0 12px}
.price-list{position:absolute;left:24px;top:988px;list-style:none;font-size:32px;font-weight:900;line-height:58px;white-space:nowrap}
.price-list .amount{font-family:"M PLUS Rounded 1c",sans-serif;font-size:44px}
.price-list .unit{font-size:26px}
.price-list .note{font-size:18px}
.burst{position:absolute;left:652px;top:840px;width:190px;height:190px}
.burst-text{position:absolute;left:652px;top:880px;width:190px;text-align:center;font-weight:900;line-height:1.25}
.burst-text .small{font-size:20px}
.burst-text .big{font-size:44px;color:var(--yellow)}
.mission{position:absolute;left:22px;top:1140px;font-size:22px;font-weight:900;line-height:32px;display:flex;align-items:center;gap:8px;white-space:nowrap}
</style>
</head>
<body>
<main class="flyer">
  <p class="tagline">熊本県八代市の地域情報ポータルサイト『セム』</p>
  <h1 class="site-name">SEMU</h1>

  <div class="model-photo" role="img" aria-label="スマートフォンを指さして微笑む女性の写真"></div>

  <svg class="bubble" viewBox="0 0 450 175" aria-hidden="true">
    <path d="M55 5 H435 Q447 5 447 17 V158 Q447 170 435 170 H67 Q55 170 55 158 V100 L0 88 L55 72 V17 Q55 5 67 5 Z" fill="#ffffff"/>
  </svg>
  <p class="bubble-text">あなたの<span class="accent">店舗</span>を<br>掲載してみませんか？</p>

  <div class="phone"></div>
  <div class="phone-screen" role="img" aria-label="セムのサイト画面、料理写真と店舗情報の一覧"></div>
  <div class="phone-button"></div>

  <ul class="genre-list">
    <li><span class="tag">グルメ</span></li>
    <li><span class="tag">ファッション</span></li>
    <li><span class="tag">イベント</span></li>
    <li><span class="tag">求人</span> まで、</li>
    <li>八代の情報が満載！</li>
  </ul>

  <p class="price-label">店舗情報掲載料</p>
  <ul class="price-list">
    <li>1ページ……… <span class="amount">21,000</span><span class="unit">円/年</span></li>
    <li>複数ページ… <span class="amount">42,000</span><span class="unit">円/年</span> <span class="note">(写真・メニュー・クーポン等)</span></li>
  </ul>

  <svg class="burst" viewBox="0 0 200 200" aria-hidden="true">
    <polygon fill="#e60012" points="100,0 117,28 148,12 150,46 186,44 170,74 200,100 170,126 186,156 150,154 148,188 117,172 100,200 83,172 52,188 50,154 14,156 30,126 0,100 30,74 14,44 50,46 52,12 83,28"/>
  </svg>
  <p class="burst-text"><span class="small">求人情報掲載</span><br><span class="big">無料</span><br><span class="small">採用時31,500円</span></p>

  <p class="mission">
    <svg width="24" height="24" viewBox="0 0 28 28" aria-hidden="true"><polygon points="4,4 24,14 4,24" fill="#fff100"/></svg>
    当サイトの収益は児童養護施設等の子供達の学習支援に使われます！
  </p>
</main>
</body>
</html>
```